Menu Design for Indian Restaurant

We are a new Indian restaurant, named Saffron Lantern Restaurant, looking for a sophisticated looking menu. It is a semi-formal dining restaurant with wooden tables and chairs and will have a focus on a creating a lively atmosphere. Environment-friendly products will be used, and the menu will be 100% vegetarian. There will be an emphasis on fresh, healthy and delicious food. We will be targeting vegans, vegetarians, health conscious people, people from all age groups, Indians, Australian's as well as other ethnic communities. We need a clean, simple, sophisticated design for the new restaurant menu. Attached is the restaurant logo for reference.

UPDATE:
- We have attached the menu
- We are not looking for any particular type of layout or size (open to suggests). Please suggest this after having a look at the menu contents. However, we will be having one formal menu to be used in the restaurant, and one in brochure form for distribution.
- There are no images at present. If you feel the need of images, please use sample images for now.

Thank you for the entries thus far.
Updates

Target Market(s)

All age groups from different nationalities

Industry/Entity Type

Indian Restaurant

Colors

Designer to choose colors to be used in the design.

Requirements
Nice to have
• This will be printed on environmentally friendly paper.

```html
<!DOCTYPE html>
<html lang="en">
<head>
<meta charset="utf-8">
<title>Saffron Lantern Restaurant – Menu</title>
<link href="https://fonts.googleapis.com/css2?family=Oswald:wght@500&family=Roboto+Condensed:wght@300;400&family=Playfair+Display:wght@400&display=swap" rel="stylesheet">
<style>
:root{
  --paper:#ffffff;
  --ink:#3d2a20;
  --text:#5b5550;
  --gold:#c9a66b;
  --gold-soft:#eadcbf;
  --saffron:#f08a24;
  --green:#2f8c3c;
}
*{margin:0;padding:0;box-sizing:border-box}
html,body{width:687px;height:1200px;overflow:hidden;background:var(--paper)}
.menu{position:relative;width:687px;height:1200px;background:var(--paper);font-family:"Roboto Condensed",sans-serif;color:var(--text)}
.ornament{position:absolute}
.ornament--top-left{left:0;top:0;width:200px;height:370px;background:radial-gradient(ellipse at 0 0,var(--gold-soft) 0%,rgba(234,220,191,.55) 45%,rgba(255,255,255,0) 75%)}
.ornament--top-right{right:0;top:0;width:200px;height:560px;background:radial-gradient(ellipse at 100% 20%,var(--gold-soft) 0%,rgba(234,220,191,.5) 45%,rgba(255,255,255,0) 78%)}
.ornament--left{left:0;bottom:0;width:190px;height:440px;background:radial-gradient(ellipse at 0 70%,var(--gold-soft) 0%,rgba(234,220,191,.55) 45%,rgba(255,255,255,0) 78%)}
.ornament--bottom-right{right:0;bottom:0;width:130px;height:130px;background:radial-gradient(circle at 100% 100%,var(--gold-soft) 0%,rgba(234,220,191,.5) 50%,rgba(255,255,255,0) 80%)}
.brand{position:absolute;left:0;right:0;top:52px;text-align:center}
.brand__mark{display:block;margin:0 auto}
.brand__name{margin-top:14px;font-family:"Playfair Display",serif;font-size:22px;color:var(--ink);letter-spacing:.3px}
.column{position:absolute}
.column--left{left:62px;top:372px;width:260px}
.column--right{left:372px;top:570px;width:240px;text-align:center}
.section-title{font-family:"Oswald",sans-serif;font-weight:500;font-size:14px;color:var(--ink);letter-spacing:.4px;text-transform:uppercase}
.section-title small{font-family:"Roboto Condensed",sans-serif;font-size:9px;font-weight:300;text-transform:none;letter-spacing:0;color:var(--text)}
.item{margin-top:10px}
.item__desc{font-size:9px;font-weight:300;line-height:13px}
.item__name{font-size:11.5px;line-height:15px;color:var(--ink)}
.column--left .section-title + .item{margin-top:12px}
.column--left .section--pizza{margin-top:22px}
.column--right .item{margin-top:9px}
.soup .item__name{margin-top:2px}
.tapas{margin-top:14px}
</style>
</head>
<body>
<main class="menu">
  <div class="ornament ornament--top-left" role="img" aria-label="Gold mandala and paisley ornament in the top left corner"></div>
  <div class="ornament ornament--top-right" role="img" aria-label="Gold mandala ornament along the top right edge"></div>
  <div class="ornament ornament--left" role="img" aria-label="Large gold paisley ornament along the lower left edge"></div>
  <div class="ornament ornament--bottom-right" role="img" aria-label="Small gold corner ornament"></div>

  <header class="brand">
    <svg class="brand__mark" width="88" height="88" viewBox="0 0 88 88" aria-hidden="true">
      <circle cx="44" cy="44" r="40" fill="none" stroke="var(--gold)" stroke-width="3"/>
    </svg>
    <h1 class="brand__name">Saffron Lantern Restaurant</h1>
  </header>

  <section class="column column--left">
    <div class="section--burger">
      <h2 class="section-title">Burger Parade <small>served with spicy potatoes fries</small></h2>
      <div class="item"><p class="item__desc">Vegetables potatoes patty beetroot carrot onion lettuce</p><p class="item__name">7.9 Grass Hopper</p></div>
      <div class="item"><p class="item__desc">Potato cottage cheese patty tomato capsicum cucumber lettuce cheese</p><p class="item__name">7.9 Cheese Hopper</p></div>
    </div>
    <div class="section--pizza">
      <h2 class="section-title">Pizza <small>medium size</small></h2>
      <div class="item"><p class="item__desc">Pineapple capsicum marjoram grilled black olive tomato cheese</p><p class="item__name">11.9 Tropicana</p></div>
      <div class="item"><p class="item__desc">Jalapeño capsicum tomato mushrooms black olive cheese</p><p class="item__name">12.9 Mexicana</p></div>
      <div class="item"><p class="item__desc">Greek cheese capsicum red Kalamata olives onion tomato cheese</p><p class="item__name">12.9 Kalamata</p></div>
      <div class="item"><p class="item__desc">Sun dry tomato green olive artichoke fresh parsley cheese</p><p class="item__name">12.9 Sicilliana</p></div>
      <div class="item"><p class="item__desc">Cottage cheese tomato capsicum onion cheese</p><p class="item__name">12.9 Indiana</p></div>
    </div>
  </section>

  <section class="column column--right">
    <div class="soup">
      <h2 class="section-title">Soup of the Day</h2>
      <p class="item__name">4.9 Cream of tomato with crotons</p>
      <p class="item__name">4.9 Curried pumpkin with shallots</p>
    </div>
    <div class="tapas">
      <h2 class="section-title">Entrée Tapas</h2>
      <div class="item"><p class="item__desc">Crispy potatoes curry leaves lotus stem ginger fresh coriander fresh chilli spice croquets</p><p class="item__name">6.9 (4pcs) Kamal Kofta</p></div>
      <div class="item"><p class="item__desc">Fresh baby spinach ricotta cheese mash potatoes ginger fresh coriander fresh chilli patty</p><p class="item__name">6.9 (4pcs) Hara Kebab</p></div>
      <div class="item"><p class="item__desc">Crispy mango pickle marinated flavoured cheddar ginger garlic cauliflower and broccoli</p><p class="item__name">6.9 (5pcs) Tandoori Foul</p></div>
      <div class="item"><p class="item__desc">Cup mushroom yogurt spice cheese fresh mint coriander cream capsicum</p><p class="item__name">7.9 (4pcs) Tandoori Mushrooms</p></div>
      <div class="item"><p class="item__desc">Vegetable stuffed pastry steamed serve with homemade chilli sauce</p><p class="item__name">6.9 (4pcs) Momos</p></div>
      <div class="item"><p class="item__desc">Vegetable momos, yoghurt, ginger, garlic cooked in clay oven</p><p class="item__name">7.9(6pcs) Tandoori Momos</p></div>
      <div class="item"><p class="item__desc">Pastry stuffed with mushrooms, steamed homemade chilli sauce</p><p class="item__name">6.9 (4pcs) Mushroom Momos</p></div>
      <div class="item"><p class="item__desc">Cottage cheese gram flour roast chilli flavoured yogurt</p><p class="item__name">7.9 (4pcs) Paneer Tikka</p></div>
      <div class="item"><p class="item__desc">Chickpeas mince raw mango powder green salsa</p><p class="item__name">6.9 (4pcs) Kabuli Tikki</p></div>
      <div class="item"><p class="item__desc">Crispy pastry stuffed potatoes peas on chickpeas</p><p class="item__name">6.9 (2pcs) Samosa Chat</p></div>
      <div class="item"><p class="item__desc">Potato patty fresh coriander cumin seed pea flour on chickpeas</p><p class="item__name">6.9 (2pcs) Aloo Tikki Chat</p></div>
      <div class="item"><p class="item__desc">Crispy pastry lentil dumpling yogurt date and mint chutney</p><p class="item__name">6.9 Dhai Bhalla Papdi</p></div>
    </div>
  </section>
</main>
</body>
</html>
```